Halverd Haul Away Start-Up Flyer

My company provides junk removal and small demolition services. I need a flyer that is modern, simple but catches the eye. Clearly shows what my company is about. I provided two uploaded files, one with out logo and the other with the logo and slogan. I would like the flyer size to be a full page (8.5"x10.98"). I also provided a list of services my company offers. I would like to incorporate a $50 Coupon for Junk Removal Service and $100 Coupon for Demolition Service at the bottom of the flyer. These flyers will be the first mailed out and be my initial entry into the market. Thank you for your time.
Target Market(s)
Home owners, Contractors, ages 30-65
Industry/Entity Type
Junk Removal
Requirements
Must have
- The company website, www.HalverdHaulAway.example
- Address: PO BOX 642 Great River, NY 11702
- Phone Number: (631) 555-0187
- Email: HalverdHaulAway@mailbox.example
- Must be a full page size, coupons mentioned above, company logo and slogan. Clearly show what the company does in a clean, modern, eye poping way.
- Must state that the company is veteran owned and operated, a small picture or graphic on the bottom would be fine. Below is a list of all services offered that must be on flyer:
- JUNK REMOVAL SERVICES:
- CONCRETE REMOVAL
- DEMOLITION REMOVAL
- APPLIANCE REMOVAL
- CARPET REMOVAL
- COMPUTER RECYCLING
- CONSTRUCTION CLEANOUT
- DUMPSTER ALTERNATIVE
- ESTATE CLEANOUT
- BASEMENT CLEANOUT
- GARAGE CLEANOUT
- ATTIC CLEANOUT
- STORAGE UNIT CLEANOUT
- FURNITURE REMOVAL
- GARBAGE REMOVAL ALTERNATIVE
- LEAF REMOVAL
- MATTRESS REMOVAL
- MONITOR RECYLING
- PRINTER RECYLING
- RUBBISH REMOVAL
- REFRIGERATOR REMOVAL
- TRASH REMOVAL
- TV RECYCLE
- TIRE RECYCLE
- *no hazerdous material
- DEMOLITION SERVICES:
- SHED RIP OUT & REMOVAL
- KITCHEN RIP OUT & REMOVAL
- BATHROOM RIP OUT & REMOVAL
- WHOLE HOUSE RIP OUT & REMOVAL
- DECK REMOVAL
- HOT TUB REMOVAL
- POOL REMOVAL
- RENOVATION PREP RIP OUTS
- *no whole house knock downs
- RESIDENTIAL:
- PLOW DRIVEWAYS
- SHOVEL OUT STAIRWAYS
- SNOW BLOW WALKWAYS/PATHS
- SALT SPREAD DRIVEWAYS/ WALKWAYS/ PATHS/ STAIRS
Nice to have
- It would be nice if the color scheme incorparated colors from my bussiness cards. I upladed a picture of one of them as a reference. As far as colors, I am a fan of any and all earth tones.

```html
<!DOCTYPE html>
<html lang="en">
<head>
<meta charset="utf-8">
<title>Halverd Haul Away Flyer</title>
<link rel="stylesheet" href="https://fonts.googleapis.com/css2?family=Open+Sans:wght@400;600;700&family=Roboto:wght@700;900&family=Roboto+Condensed:wght@400;700&display=swap">
<style>
  :root {
    --paper: #f6f5f4;
    --salmon: #ec8a80;
    --salmon-soft: #f3b3ac;
    --red: #d8342c;
    --red-deep: #b9221c;
    --ink: #2c2c2c;
    --charcoal: #2f2d2b;
    --white: #ffffff;
    --ring: #e6e3e1;
  }
  html, body { margin: 0; padding: 0; overflow: hidden; }
  body { width: 900px; height: 1200px; background: var(--paper); }
  .flyer {
    position: relative; width: 900px; height: 1200px; overflow: hidden;
    background: radial-gradient(circle at 45% 55%, #ffffff 0%, var(--paper) 70%);
    font-family: "Open Sans", Arial, sans-serif; color: var(--ink);
  }
  .disc { position: absolute; border-radius: 50%; }
  .disc--top-right { left: 590px; top: -80px; width: 300px; height: 300px; background: var(--salmon); }
  .disc--left { left: -80px; top: 290px; width: 340px; height: 340px; background: var(--salmon); }
  .disc--bottom-right { left: 610px; top: 600px; width: 340px; height: 340px; background: var(--salmon-soft); }
  .disc--bottom-small { left: 540px; top: 930px; width: 170px; height: 170px; background: var(--salmon-soft); opacity: .7; }
  .mark-ring {
    position: absolute; left: 335px; top: 680px; width: 260px; height: 260px;
    border-radius: 50%; border: 26px solid var(--ring); box-sizing: border-box; opacity: .5;
  }
  .brand {
    position: absolute; left: 36px; top: 30px; width: 200px; height: 110px;
    background: var(--charcoal); padding: 12px 14px; box-sizing: border-box; z-index: 2;
  }
  .brand__top { display: flex; align-items: center; gap: 10px; }
  .brand__dot { width: 22px; height: 22px; border-radius: 50%; background: var(--salmon); flex: none; }
  .brand__name { font-family: "Roboto", Arial, sans-serif; font-weight: 700; font-size: 22px; color: var(--white); line-height: 1.05; }
  .brand__slogan { margin: 8px 0 0; font-family: "Roboto Condensed", Arial, sans-serif; font-size: 12px; line-height: 14px; color: var(--salmon-soft); }
  .photo {
    position: absolute; border-radius: 50%; border: 8px solid var(--white);
    box-shadow: 0 4px 12px rgba(0,0,0,.25); box-sizing: border-box;
  }
  .photo--boxes { left: 240px; top: 20px; width: 290px; height: 290px; background: radial-gradient(circle at 40% 40%, #c9a77a, #6a7f9a); }
  .photo--machine { left: 490px; top: 140px; width: 300px; height: 300px; background: radial-gradient(circle at 55% 45%, #e2c23a, #7d7a70); }
  .photo--leaves { left: 105px; top: 265px; width: 350px; height: 350px; background: radial-gradient(circle at 45% 50%, #e58a2c, #9c3a22); }
  .photo--worker { left: 360px; top: 420px; width: 200px; height: 200px; background: radial-gradient(circle at 50% 45%, #8aa36a, #5b5f5c); }
  .services__title {
    position: absolute; left: 45px; top: 636px; margin: 0; width: 210px; height: 50px;
    background: var(--charcoal); color: var(--white);
    font-family: "Roboto", Arial, sans-serif; font-weight: 700; font-size: 34px; line-height: 50px; padding-left: 14px; box-sizing: border-box;
  }
  .service-group { position: absolute; font-family: "Roboto Condensed", Arial, sans-serif; }
  .service-group--junk { left: 45px; top: 700px; width: 375px; }
  .service-group--demo { left: 430px; top: 700px; width: 185px; }
  .service-group--home { left: 45px; top: 952px; width: 245px; }
  .service-group__title { margin: 0 0 4px; font-size: 15px; line-height: 18px; font-weight: 700; color: var(--red-deep); text-transform: uppercase; }
  .service-group__list { list-style: none; margin: 0; padding: 0; }
  .service-group--junk .service-group__list { columns: 2; column-gap: 5px; }
  .service-group__list li { position: relative; font-size: 14px; line-height: 18px; padding-left: 12px; break-inside: avoid; }
  .service-group__list li::before { content: ""; position: absolute; left: 1px; top: 7px; width: 5px; height: 5px; border-radius: 50%; background: var(--ink); }
  .service-group__list li.note { font-style: italic; color: var(--red-deep); }
  .service-group__list li.note::before { display: none; }
  .veteran {
    position: absolute; left: 45px; top: 1100px; width: 240px; height: 70px;
    background: var(--charcoal); color: var(--white); display: flex; align-items: center; gap: 12px;
    padding: 0 14px; box-sizing: border-box;
  }
  .veteran__star { flex: none; }
  .veteran__text { font-family: "Roboto", Arial, sans-serif; font-weight: 700; font-size: 17px; line-height: 20px; text-transform: uppercase; }
  .coupon { position: absolute; left: 620px; top: 755px; width: 260px; height: 260px; }
  .coupon__text {
    position: absolute; inset: 0; display: flex; flex-direction: column; justify-content: center; align-items: center;
    color: var(--white); font-weight: 700; text-align: center; line-height: 1.1;
  }
  .coupon__row { display: flex; align-items: baseline; gap: 6px; font-size: 15px; }
  .coupon__amount { font-family: "Roboto", Arial, sans-serif; font-size: 36px; font-weight: 900; }
  .coupon__for { font-size: 15px; margin: 2px 0 10px; }
  .contact {
    position: absolute; left: 300px; top: 1010px; width: 440px; height: 190px;
    background: var(--red); color: var(--white); text-align: center; box-sizing: border-box;
    padding-top: 28px; font-size: 19px; font-weight: 600; line-height: 33px;
  }
  .contact p { margin: 0; }
</style>
</head>
<body>
<main class="flyer">
  <div class="disc disc--top-right"></div>
  <div class="disc disc--left"></div>
  <div class="disc disc--bottom-right"></div>
  <div class="disc disc--bottom-small"></div>
  <div class="mark-ring"></div>

  <header class="brand">
    <div class="brand__top">
      <span class="brand__dot"></span>
      <span class="brand__name">Halverd<br>Haul Away</span>
    </div>
    <p class="brand__slogan">We haul it all, so you don't have to.</p>
  </header>

  <div class="photo photo--boxes" role="img" aria-label="Photo of stacked cardboard boxes and bagged junk"></div>
  <div class="photo photo--machine" role="img" aria-label="Photo of a yellow excavator on a demolition site"></div>
  <div class="photo photo--leaves" role="img" aria-label="Photo of a rake in a pile of autumn leaves"></div>
  <div class="photo photo--worker" role="img" aria-label="Photo of a crew member clearing debris"></div>

  <h2 class="services__title">Service</h2>

  <section class="service-group service-group--junk">
    <h3 class="service-group__title">Junk Removal</h3>
    <ul class="service-group__list">
      <li>Concrete removal</li>
      <li>Demolition removal</li>
      <li>Appliance removal</li>
      <li>Carpet removal</li>
      <li>Computer recycling</li>
      <li>Construction cleanout</li>
      <li>Dumpster alternative</li>
      <li>Estate cleanout</li>
      <li>Basement cleanout</li>
      <li>Garage cleanout</li>
      <li>Attic cleanout</li>
      <li>Storage unit cleanout</li>
      <li>Furniture removal</li>
      <li>Garbage removal alternative</li>
      <li>Leaf removal</li>
      <li>Mattress removal</li>
      <li>Monitor recycling</li>
      <li>Printer recycling</li>
      <li>Rubbish removal</li>
      <li>Refrigerator removal</li>
      <li>Trash removal</li>
      <li>TV recycling</li>
      <li>Tire recycling</li>
      <li class="note">*No hazardous material</li>
    </ul>
  </section>

  <section class="service-group service-group--demo">
    <h3 class="service-group__title">Demolition</h3>
    <ul class="service-group__list">
      <li>Shed rip out &amp; removal</li>
      <li>Kitchen rip out &amp; removal</li>
      <li>Bathroom rip out &amp; removal</li>
      <li>Whole house rip out &amp; removal</li>
      <li>Deck removal</li>
      <li>Hot tub removal</li>
      <li>Pool removal</li>
      <li>Renovation prep rip outs</li>
      <li class="note">*No whole house knock downs</li>
    </ul>
  </section>

  <section class="service-group service-group--home">
    <h3 class="service-group__title">Residential</h3>
    <ul class="service-group__list">
      <li>Plow driveways</li>
      <li>Shovel out stairways</li>
      <li>Snow blow walkways / paths</li>
      <li>Salt spread driveways, walkways, stairs</li>
    </ul>
  </section>

  <div class="veteran">
    <svg class="veteran__star" width="34" height="34" viewBox="0 0 34 34" aria-hidden="true">
      <polygon fill="var(--salmon)" points="17,1 21,12 33,12 23,19 27,31 17,24 7,31 11,19 1,12 13,12"/>
    </svg>
    <span class="veteran__text">Veteran Owned<br>&amp; Operated</span>
  </div>

  <div class="coupon">
    <svg width="260" height="260" viewBox="0 0 260 260" aria-hidden="true">
      <polygon fill="var(--red-deep)" points="130,0 148,32 180,10 186,47 224,40 213,77 250,84 224,112 260,130 224,148 250,176 213,183 224,220 186,213 180,250 148,228 130,260 112,228 80,250 74,213 36,220 47,183 10,176 36,148 0,130 36,112 10,84 47,77 36,40 74,47 80,10 112,32"/>
    </svg>
    <div class="coupon__text">
      <div class="coupon__row"><span class="coupon__amount">$50</span><span>Coupon for</span></div>
      <div class="coupon__for">Junk Removal Service</div>
      <div class="coupon__row"><span class="coupon__amount">$100</span><span>Coupon for</span></div>
      <div class="coupon__for">Demolition Service</div>
    </div>
  </div>

  <footer class="contact">
    <p>www.HalverdHaulAway.example</p>
    <p>PO BOX 642 Great River, NY 11702</p>
    <p>(631) 555-0187</p>
    <p>HalverdHaulAway@mailbox.example</p>
  </footer>
</main>
</body>
</html>
```